Design some Business Cards

Looking for a very creative and unique design for a business card for a marketing firm. Needs to include the following:

Logo
URL: http://www.TheVellinorGroup.com
Businesss Phone: 555-318-4706

Then it will need to be customized with individual contact info:
Name
Mobile #
E-mail

Do not include address

Logo attached

```html
<!DOCTYPE html>
<html lang="en">
<head>
<meta charset="utf-8">
<title>The Vellinor Group – Business Cards</title>
<link href="https://fonts.googleapis.com/css2?family=Open+Sans:wght@400;600;700&display=swap" rel="stylesheet">
<style>
  :root {
    --bg: #e9e6e1;
    --card: #ffffff;
    --ink: #0c0c0c;
    --band: #050505;
    --accent-red: #d8262c;
    --brand-blue: #1e6a9a;
    --brand-grey: #5b5b5b;
    --on-dark: #ffffff;
  }
  html, body {
    margin: 0;
    width: 1200px;
    height: 900px;
    overflow: hidden;
    background: var(--bg);
    font-family: "Open Sans", Arial, sans-serif;
  }
  .canvas { position: relative; width: 1200px; height: 900px; }

  .card {
    position: absolute;
    left: 236px;
    width: 693px;
    background: var(--card);
    box-shadow: 0 2px 6px rgba(0,0,0,0.18);
    overflow: hidden;
  }
  .card--front { top: 63px; height: 353px; }
  .card--back  { top: 457px; height: 360px; }

  .brand {
    position: absolute;
    display: flex;
    align-items: center;
    gap: 14px;
  }
  .brand__dot {
    border-radius: 50%;
    border: 4px solid var(--brand-grey);
    box-sizing: border-box;
  }
  .brand__name {
    color: var(--brand-blue);
    font-weight: 700;
    text-transform: uppercase;
    letter-spacing: 0.5px;
    white-space: nowrap;
  }
  .card--front .brand { left: 213px; top: 38px; }
  .card--front .brand__dot { width: 60px; height: 60px; }
  .card--front .brand__name { font-size: 22px; }

  .card--back .brand { left: 130px; top: 130px; }
  .card--back .brand__dot { width: 96px; height: 96px; border-width: 6px; }
  .card--back .brand__name { font-size: 36px; }

  .rule-red {
    position: absolute;
    left: 0; right: 0;
    height: 2px;
    background: var(--accent-red);
  }
  .rule-red--top { top: 170px; }
  .rule-red--bottom { top: 342px; }

  .band {
    position: absolute;
    left: 0; right: 0;
    top: 177px;
    height: 160px;
    background: var(--band);
    color: var(--on-dark);
  }
  .person { position: absolute; left: 4px; top: 50px; width: 296px; }
  .person__name {
    font-size: 37px;
    font-weight: 400;
    line-height: 1;
    white-space: nowrap;
  }
  .person__title {
    margin-top: 8px;
    font-size: 10px;
    text-align: right;
    padding-right: 4px;
  }
  .band__divider {
    position: absolute;
    left: 307px; top: 16px;
    width: 3px; height: 127px;
    background: var(--on-dark);
  }
  .contacts {
    position: absolute;
    left: 328px; top: 18px;
    margin: 0; padding: 0;
    list-style: none;
  }
  .contacts li {
    display: flex;
    align-items: center;
    gap: 12px;
    height: 44px;
    font-size: 22px;
    white-space: nowrap;
  }
  .contacts svg { width: 32px; height: 32px; flex: none; }
</style>
</head>
<body>
<div class="canvas">

  <section class="card card--front">
    <div class="brand">
      <span class="brand__dot"></span>
      <span class="brand__name">The Vellinor Group</span>
    </div>

    <div class="rule-red rule-red--top"></div>
    <div class="band">
      <div class="person">
        <div class="person__name">JONATHAN DOE</div>
        <div class="person__title">FOUNDER AND CEO</div>
      </div>
      <div class="band__divider"></div>
      <ul class="contacts">
        <li>
          <svg viewBox="0 0 32 32" aria-hidden="true">
            <circle cx="16" cy="16" r="14" fill="none" stroke="#fff" stroke-width="2"/>
            <path d="M11 9l3 0 1.5 4-2 1.5c1 2 2.5 3.5 4.5 4.5l1.5-2 4 1.5 0 3c0 1-1 1.5-2 1.5-6 -0.5-11-5.5-11.5-11.5 0-1 0.5-2 1-2.5z" fill="#fff"/>
          </svg>
          <span>+1 555-318-4706</span>
        </li>
        <li>
          <svg viewBox="0 0 32 32" aria-hidden="true">
            <circle cx="16" cy="16" r="15" fill="#fff"/>
            <rect x="8" y="10.5" width="16" height="11" fill="none" stroke="#000" stroke-width="1.8"/>
            <path d="M8 10.5l8 6.5 8-6.5" fill="none" stroke="#000" stroke-width="1.8"/>
          </svg>
          <span>Info@TheVellinorGroup.com</span>
        </li>
        <li>
          <svg viewBox="0 0 32 32" aria-hidden="true">
            <circle cx="16" cy="16" r="15" fill="#fff"/>
            <g fill="none" stroke="#000" stroke-width="1.5">
              <circle cx="16" cy="16" r="9"/>
              <ellipse cx="16" cy="16" rx="4" ry="9"/>
              <path d="M7 16h18M8.5 11.5h15M8.5 20.5h15"/>
            </g>
          </svg>
          <span>www.TheVellinorGroup.com</span>
        </li>
      </ul>
    </div>
    <div class="rule-red rule-red--bottom"></div>
  </section>

  <section class="card card--back">
    <div class="brand">
      <span class="brand__dot"></span>
      <span class="brand__name">The Vellinor Group</span>
    </div>
  </section>

</div>
</body>
</html>
```